Business Card design for a company called Tallow Flame NI

I need a business card design for my oil fired boiler servicing company. I have a logo design already and Im just looking that incorporated into the business card design. card details; Tallow Flame NI
Oil Burner Servicing - Mid Ulster Area
Service Engineer - Owen Marsh
Mobile 07751364927
email - Tallow.Flame.NI@hearthmail.example
www.tallowflameni.example
I carry out Servicing, Commissioning, Fault Finding, Warranty Validation
Target Market(s)
home owners with oil fired central heating
Industry/Entity Type
Business
Contact Information for Business Card
Tallow Flame NI
Tell. 07751364927
Web: www.tallowflameni.example
email Tallow.Flame.NI@Hearthmail.Example
Servicing Fault Finding Commissioning Warranty Validation
Look and feel

```html
<!DOCTYPE html>
<html lang="en">
<head>
<meta charset="utf-8">
<title>Tallow Flame NI – Business Card</title>
<link rel="stylesheet" href="https://fonts.googleapis.com/css2?family=PT+Sans:wght@400;700&family=Nunito+Sans:wght@700&display=swap">
<style>
  :root {
    --backdrop: #000000;
    --card: #2f3033;
    --card-edge: #35363a;
    --green: #6cc04a;
    --green-deep: #3fae49;
    --text-light: #f2f2f2;
    --divider: #3c3d41;
  }
  * { margin: 0; padding: 0; box-sizing: border-box; }
  html, body {
    width: 1200px; height: 900px; overflow: hidden;
    background: var(--backdrop);
  }
  .canvas { position: relative; width: 1200px; height: 900px; }

  .card {
    position: absolute;
    top: 271px;
    width: 457px; height: 281px;
    border-radius: 14px;
    overflow: hidden;
    background: linear-gradient(160deg, var(--card-edge), var(--card) 60%);
    font-family: "PT Sans", sans-serif;
  }
  .card--front { left: 137px; }
  .card--back { left: 626px; }

  /* front */
  .brand-stack {
    position: absolute; left: 28px; top: 60px; width: 134px;
    display: flex; flex-direction: column; align-items: center; gap: 12px;
  }
  .brand-dot {
    width: 64px; height: 64px; border-radius: 50%;
    background: var(--green-deep);
  }
  .brand-name--small {
    color: var(--green); font-weight: 700; font-size: 15px;
    text-align: center; line-height: 1.15; white-space: nowrap;
  }
  .divider {
    position: absolute; left: 182px; top: 54px;
    width: 1px; height: 138px; background: var(--divider);
  }
  .right-column { position: absolute; left: 203px; top: 58px; right: 24px; }
  .person__name { color: var(--green); font-size: 18px; font-weight: 700; line-height: 1.1; }
  .person__role { color: var(--text-light); font-size: 13px; line-height: 1.4; }

  .contacts { list-style: none; margin-top: 22px; }
  .contacts li {
    display: flex; align-items: center; gap: 8px;
    color: var(--text-light); font-size: 11.5px; height: 19px;
    white-space: nowrap;
  }
  .contacts svg { width: 10px; height: 10px; fill: var(--green); flex: none; }

  .services {
    position: absolute; left: 0; right: 0; top: 217px;
    text-align: center; color: var(--green);
    font-size: 13.5px; font-weight: 700; line-height: 19px;
  }

  /* back */
  .lockup {
    position: absolute; left: 63px; top: 101px;
    display: flex; align-items: center; gap: 12px;
  }
  .lockup__dot {
    width: 78px; height: 78px; border-radius: 50%;
    background: var(--green-deep);
    flex: none;
  }
  .brand-name--large {
    font-family: "Nunito Sans", sans-serif;
    color: var(--green); font-weight: 700; font-size: 32px; line-height: 1;
    white-space: nowrap;
  }
  .tagline {
    margin-top: 6px;
    font-family: "Nunito Sans", sans-serif;
    color: var(--green); font-weight: 700; font-size: 8.5px;
    letter-spacing: 1.1px; text-transform: uppercase; white-space: nowrap;
  }
</style>
</head>
<body>
<main class="canvas">

  <section class="card card--front" aria-label="Card front">
    <div class="brand-stack">
      <span class="brand-dot"></span>
      <span class="brand-name--small">Tallow Flame NI</span>
    </div>
    <span class="divider"></span>

    <div class="right-column">
      <div class="person">
        <p class="person__name">Owen Marsh</p>
        <p class="person__role">Service Engineer</p>
      </div>

      <ul class="contacts">
        <li>
          <svg viewBox="0 0 10 10"><path d="M2 0.5 L3.6 2.6 L2.8 3.6 C3.4 4.9 4.9 6.4 6.3 7.1 L7.3 6.3 L9.5 7.9 L8.4 9.5 C4.2 9.2 0.8 5.8 0.5 1.6 Z"/></svg>
          <span>07751364927</span>
        </li>
        <li>
          <svg viewBox="0 0 10 10"><path d="M0.5 2 H9.5 V8.5 H0.5 Z M1 2.4 L5 5.4 L9 2.4 V3.2 L5 6.2 L1 3.2 Z" fill-rule="evenodd"/></svg>
          <span>Tallow.Flame.NI@Hearthmail.Example</span>
        </li>
        <li>
          <svg viewBox="0 0 10 10"><circle cx="5" cy="5" r="4.5"/></svg>
          <span>www.tallowflameni.example</span>
        </li>
      </ul>
    </div>

    <p class="services">Servicing | Fault Finding | Commissioning<br>Warranty Validation</p>
  </section>

  <section class="card card--back" aria-label="Card back">
    <div class="lockup">
      <span class="lockup__dot"></span>
      <div>
        <p class="brand-name--large">Tallow Flame NI</p>
        <p class="tagline">Oil Burner Servicing - Mid Ulster Area</p>
      </div>
    </div>
  </section>

</main>
</body>
</html>
```